Baby Boutique Needs a Business Card Design

We need a modern double sided business card design using the attached logo for T' Tot Nook.

T' Tot Nook is a baby boutique which sells only handmade clothing and accessories for both boys and girls. Our store will live exclusively online.

We would like to only use the colors that have been used in the logo.

Target Market(s)

Potential wholesale clients, Small business owners

Industry/Entity Type

Retail

Contact Information for Business Card

Name Benedict R. Halvorsen (Owner)
Email sales@ttotnook.example
Main Phone 555-203-7164
Cell phone 555-203-7590
Website www.TTotNook.example

Font styles to use
Sans Serif

Colors

Designer to choose colors to be used in the design.

Requirements
Must have
• -Would like to have icons that indentify the contact information.
• -Include our website
• -Include our tagline in a small area near the bottom. "Handmade Baby Creations"
• -Would like to include Facebook and Instagram Icons
• -
Nice to have
• Would like to have a simple back side with the logo.
• Something along the lines of the meridale funding card attached.

```html
<!DOCTYPE html>
<html lang="en">
<head>
<meta charset="utf-8">
<title>T' Tot Nook — Business Card</title>
<link rel="stylesheet" href="https://fonts.googleapis.com/css2?family=Kaushan+Script&family=Roboto:wght@400;500;700&display=swap">
<style>
  :root {
    --coral: #de4f4f;
    --teal: #6ac8b8;
    --paper: #ffffff;
    --ink: #555555;
    --stage: #ece9e4;
  }
  html, body {
    margin: 0;
    padding: 0;
    width: 1200px;
    height: 800px;
    overflow: hidden;
    background: var(--stage);
    font-family: "Roboto", Arial, sans-serif;
  }
  .canvas {
    position: relative;
    width: 1200px;
    height: 800px;
  }
  .card {
    position: absolute;
    top: 245px;
    width: 540px;
    height: 309px;
    border-radius: 4px;
    box-shadow: 0 6px 18px rgba(0,0,0,0.15);
    overflow: hidden;
  }
  .card--back {
    left: 40px;
    background: var(--coral);
    display: flex;
    align-items: center;
    justify-content: center;
  }
  .card--front {
    left: 620px;
    background: var(--paper);
  }
  .brand {
    font-family: "Roboto", Arial, sans-serif;
    font-weight: 700;
    margin: 0;
    letter-spacing: 0.5px;
  }
  .brand--back {
    color: var(--paper);
    font-size: 54px;
  }
  .brand--front {
    position: absolute;
    left: 30px;
    top: 70px;
    width: 190px;
    text-align: center;
    color: var(--teal);
    font-size: 34px;
  }
  .social {
    position: absolute;
    left: 96px;
    top: 158px;
    display: flex;
    gap: 10px;
  }
  .social__dot {
    width: 22px;
    height: 22px;
    border-radius: 50%;
    background: var(--coral);
  }
  .person {
    position: absolute;
    left: 250px;
    top: 64px;
  }
  .person__name {
    margin: 0;
    font-family: "Kaushan Script", cursive;
    font-weight: 400;
    font-size: 27px;
    color: var(--coral);
    line-height: 1.1;
  }
  .person__role {
    margin: 0;
    font-size: 14px;
    color: var(--ink);
  }
  .contacts {
    position: absolute;
    left: 252px;
    top: 146px;
    margin: 0;
    padding: 0;
    list-style: none;
  }
  .contacts li {
    display: flex;
    align-items: center;
    gap: 10px;
    font-size: 15px;
    color: var(--ink);
    height: 22px;
  }
  .contacts svg {
    width: 13px;
    height: 13px;
    fill: none;
    stroke: var(--coral);
    stroke-width: 2;
  }
  .tagline-band {
    position: absolute;
    left: 0;
    right: 0;
    bottom: 32px;
    height: 26px;
    background: var(--teal);
    color: var(--paper);
    font-size: 14px;
    display: flex;
    align-items: center;
    justify-content: center;
    letter-spacing: 0.3px;
  }
</style>
</head>
<body>
<main class="canvas">
  <section class="card card--back" aria-label="Card back">
    <p class="brand brand--back">T' Tot Nook</p>
  </section>

  <section class="card card--front" aria-label="Card front">
    <p class="brand brand--front">T' Tot Nook</p>
    <div class="social">
      <span class="social__dot" role="img" aria-label="Photo sharing profile"></span>
      <span class="social__dot" role="img" aria-label="Social network profile"></span>
    </div>

    <div class="person">
      <h1 class="person__name">Benedict R. Halvorsen</h1>
      <p class="person__role">Owner</p>
    </div>

    <ul class="contacts">
      <li>
        <svg viewBox="0 0 16 16" aria-hidden="true"><path d="M3 1.5 L6 1.5 L7 5 L5 6.5 Q6.5 9.5 9.5 11 L11 9 L14.5 10 L14.5 13 Q14.5 14.5 13 14.5 Q2 13.5 1.5 3 Q1.5 1.5 3 1.5 Z" fill="var(--coral)" stroke="none"/></svg>
        <span>555-203-7164</span>
      </li>
      <li>
        <svg viewBox="0 0 16 16" aria-hidden="true"><rect x="4" y="1.5" width="8" height="13" rx="1.5"/><line x1="7" y1="12" x2="9" y2="12"/></svg>
        <span>555-203-7590</span>
      </li>
      <li>
        <svg viewBox="0 0 16 16" aria-hidden="true"><circle cx="8" cy="8" r="6.5"/><ellipse cx="8" cy="8" rx="3" ry="6.5"/><line x1="1.5" y1="8" x2="14.5" y2="8"/></svg>
        <span>www.TTotNook.example</span>
      </li>
    </ul>

    <div class="tagline-band">Handmade Baby Creations</div>
  </section>
</main>
</body>
</html>
```